KJW - KJW - March 2018 - Advertisement 1/2 Page

I am looking to get some opinions to streamline this 1/2 page advertisement for our IT company that specializes in the medical industry and clean up and make it pop. I really want to capture the readers attention and stick out in this medical newspaper. I am looking to get some opinions to streamline this 1/2 page advertisement for our IT company that specializes in the medical industry and clean up and make it pop. I really want to capture the readers attention and stick out in this medical newspaper.

Target Market(s)

Medical / Healthcare

Industry/Entity Type

Medical

Colors
9dd4eb
33a6d7
0692cd
0255a3
3277b5
85acd3
ffffff

Requirements
Must have
• Simple and Clean look that is 1/2 page and really catches the practice manager or doctors eyes
Nice to have
• Simple and Clean look that is 1/2 page and really catches the practice manager or doctors eyes. Has the logos for the software companies is a MUST. I attached a medical flyer with the logos on it to use.
Should not have
• Less pictures of doctors

```html
<!DOCTYPE html>
<html lang="en">
<head>
<meta charset="utf-8">
<title>KJW – Medical Office Technology Solutions</title>
<link rel="stylesheet" href="https://fonts.googleapis.com/css2?family=Exo+2:wght@300;400;500;600;700&display=swap">
<style>
  :root {
    --sky: #9dd4eb;
    --azure: #33a6d7;
    --cerulean: #0692cd;
    --navy: #0255a3;
    --steel: #3277b5;
    --mist: #85acd3;
    --white: #ffffff;
    --grey: #6f7275;
    --rule-grey: #9ea3a8;
    --badge: #c9d3dc;
  }
  * { margin: 0; padding: 0; box-sizing: border-box; }
  html, body { width: 1200px; height: 848px; overflow: hidden; background: var(--white); }
  body { font-family: "Exo 2", sans-serif; position: relative; }

  .hero-panel {
    position: absolute; left: 20px; top: 20px; width: 1160px; height: 702px;
    border-radius: 34px;
    background: linear-gradient(90deg, var(--sky) 0%, var(--azure) 30%, var(--cerulean) 48%, var(--steel) 72%, var(--navy) 100%);
    overflow: hidden;
  }
  .hero-panel__accent-area {
    position: absolute; left: 100px; top: 20px; width: 300px; height: 160px;
  }

  .brand-card {
    position: absolute; left: 31px; top: 204px; width: 394px; height: 268px;
    background: var(--white); border-radius: 28px;
    text-align: center;
  }
  .brand-card__lead {
    position: absolute; left: 0; right: 0; top: 68px;
    font-size: 44px; font-weight: 400; color: var(--azure); letter-spacing: 0.5px; line-height: 1;
  }
  .brand-card__name {
    position: absolute; left: 0; right: 0; top: 134px;
    font-size: 60px; font-weight: 400; color: var(--steel); line-height: 1;
  }
  .brand-card__rule {
    position: absolute; left: 28px; right: 28px; top: 200px;
    height: 2px; background: var(--rule-grey);
  }
  .brand-card__tag {
    position: absolute; left: 0; right: 0; top: 203px;
    font-size: 12.5px; font-weight: 700; color: var(--grey); letter-spacing: 0.4px;
  }

  .pitch { position: absolute; left: 530px; top: 66px; width: 560px; color: var(--white); }
  .pitch__intro { font-size: 19.5px; font-weight: 300; line-height: 24px; letter-spacing: 0.4px; }
  .pitch__intro strong { font-weight: 700; }

  .services { position: absolute; left: 530px; top: 216px; width: 650px; }
  .services__title {
    font-size: 18px; line-height: 22px; font-weight: 600; color: var(--white); letter-spacing: 0.3px;
    padding-bottom: 2px; border-bottom: 2px dotted rgba(255,255,255,0.85);
  }
  .services__list { list-style: none; margin-top: 20px; }
  .services__list li {
    position: relative; padding-left: 25px;
    font-size: 15.5px; line-height: 20.5px; color: var(--sky); letter-spacing: 0.4px;
  }
  .services__list li::before {
    content: "•"; position: absolute; left: 1px; color: var(--white);
  }

  .reach { position: absolute; left: 530px; top: 556px; width: 650px; color: var(--white); }
  .reach__claim {
    width: 560px;
    font-size: 19.5px; font-weight: 300; line-height: 24px; letter-spacing: 0.4px;
  }
  .reach__rule { height: 0; border-bottom: 2px dotted rgba(255,255,255,0.85); }
  .reach__label { margin-top: 27px; font-size: 15px; line-height: 18px; font-weight: 400; letter-spacing: 0.3px; }
  .reach__cities { font-size: 14px; line-height: 17.5px; color: var(--sky); letter-spacing: 0.3px; }

  .contact { position: absolute; left: 76px; top: 747px; }
  .contact__phone { font-size: 45px; font-weight: 400; color: var(--cerulean); letter-spacing: 1px; line-height: 1; }
  .contact__web { margin-top: 6px; font-size: 20px; color: var(--steel); letter-spacing: 0.5px; }

  .partners {
    position: absolute; left: 528px; top: 768px; width: 620px; height: 50px;
    display: flex; align-items: center; justify-content: space-between;
  }
  .partner-badge { background: var(--badge); border-radius: 4px; }
  .partner-badge--small { width: 70px; height: 44px; }
  .partner-badge--wide { width: 84px; height: 36px; }
  .partner-badge--square { width: 46px; height: 46px; background: var(--azure); }
  .partner-badge--long { width: 140px; height: 42px; border-radius: 21px 4px 4px 21px; }

  .footer-band { position: absolute; left: 0; bottom: 0; width: 1200px; height: 8px; background: var(--cerulean); }
</style>
</head>
<body>
  <section class="hero-panel">
    <div class="hero-panel__accent-area" role="img" aria-label="Decorative accent area over the light blue gradient"></div>

    <div class="brand-card">
      <p class="brand-card__lead">It’s time to</p>
      <p class="brand-card__name">KJW</p>
      <div class="brand-card__rule"></div>
      <p class="brand-card__tag">MEDICAL OFFICE TECHNOLOGY SOLUTIONS</p>
    </div>
  </section>

  <section class="pitch">
    <p class="pitch__intro">At <strong>KJW</strong>, we are experts who have hired experts, so you get an IT guy who’s capable, precise, thorough and knows that communicating with our clients is as important as connecting the right wires. KJW keeps your office working efficiently with precision.</p>
  </section>

  <section class="services">
    <h2 class="services__title">WHAT WE DO</h2>
    <ul class="services__list">
      <li>Desktop / Server Configuration, Service &amp; Support</li>
      <li>Data / Internet / Network Configuration, Security &amp; Management</li>
      <li>Integration of Multiple Hardware &amp; Software Systems</li>
      <li>Mobile / Tablet / Smartphone Configuration &amp; Support</li>
      <li>EMR / EHR Experience, Service &amp; Support</li>
      <li>Onsite Local IT Service &amp; Support</li>
      <li>HIPAA HITECH Compliance</li>
      <li>Secure Remote Access &amp; Monitoring</li>
      <li>Anti-Virus, Anti-Spyware, Anti-Spam Solutions</li>
      <li>Firewall, VPN &amp; Email Encryption Services</li>
      <li>Onsite / Offsite Data Backup Protection</li>
      <li>Web Design, Hosting &amp; Cloud Services</li>
      <li>Remote IT Service &amp; Support</li>
    </ul>
  </section>

  <section class="reach">
    <p class="reach__claim">We work with over 250 medical practices in Alabama providing service, support, equipment sales &amp; software</p>
    <div class="reach__rule"></div>
    <p class="reach__label">SERVING</p>
    <p class="reach__cities">Anniston • Auburn • Birmingham • Decatur • Gadsden • Huntsville<br>Montgomery • Tuscaloosa &amp; surrounding areas</p>
  </section>

  <footer class="contact">
    <p class="contact__phone">800-555-0142</p>
    <p class="contact__web">www.kjwmedicalit.com</p>
  </footer>

  <div class="partners" aria-label="Technology partner badges">
    <div class="partner-badge partner-badge--small"></div>
    <div class="partner-badge partner-badge--wide"></div>
    <div class="partner-badge partner-badge--wide"></div>
    <div class="partner-badge partner-badge--square"></div>
    <div class="partner-badge partner-badge--long"></div>
  </div>

  <div class="footer-band"></div>
</body>
</html>
```